Design a label for a range of honey under :BRIGHT MEADOW HONEY. (Original quirky different)

Create a label for a range of honey products under the brand BRIGHT MEADOW HONEY.
Iam the beekeeper and want to sell for the local New Zealand market directly to the consumer, online mainly.
Brand position: A contemporary honey, a fresh look for a simple product, like nature intended, nothing taken out, nothing added. Doesnt take itself seriously.
Personality: Contemporary, fresh, modern, free and fun,loving. Doesnt take itself seriously, loving, generous, upbeat, provide enjoyment, life ...
Brand value: Straight up, keep it simple, generous, different,
Label: Modern twist of nature and goodness (no straight picture of nature) quirky?, use of slogan? ( Nature in a pot / More than just honey / Taste of nature / It's all good...
Need to stand out, make you smile, be noticed, different...

Target Market(s)

Online direct customer.

Requirements
Must have
• legal requirements for NZ labeling attached.
A twist and quirky side...
Should not have
• Basic picture of nature.
Straight forward boring everybody else's feel.

```html
<!DOCTYPE html>
<html lang="en">
<head>
<meta charset="utf-8">
<title>Bright Meadow Honey – Label</title>
<link rel="stylesheet" href="https://fonts.googleapis.com/css2?family=Cinzel:wght@400;500&family=Montserrat:wght@400;500;600&display=swap">
<style>
  :root {
    --backdrop: #5a5a5a;
    --label: #1b1b1b;
    --label-edge: #141414;
    --honey-cream: #e9d3bd;
    --text-light: #f1f1f1;
    --text-muted: #b9b9b9;
    --motif: #5e5e5e;
  }
  * { margin: 0; padding: 0; box-sizing: border-box; }
  html, body {
    width: 1159px;
    height: 1200px;
    overflow: hidden;
    background: var(--backdrop);
  }
  .canvas {
    position: relative;
    width: 1159px;
    height: 1200px;
  }
  .label {
    position: absolute;
    left: 180px;
    top: 200px;
    width: 800px;
    height: 800px;
    overflow: hidden;
    background: linear-gradient(90deg, var(--label-edge) 0%, var(--label) 30%, var(--label) 70%, var(--label-edge) 100%);
  }
  .brand-name {
    position: absolute;
    left: 76px;
    top: 170px;
    font-family: "Cinzel", serif;
    font-weight: 400;
    font-size: 90px;
    line-height: 118px;
    color: var(--honey-cream);
    letter-spacing: 0;
    white-space: nowrap;
  }
  .brand-name span { display: block; }
  .dipper-motif {
    position: absolute;
    left: 540px;
    top: 180px;
    width: 220px;
    height: 400px;
    border-radius: 110px 110px 60px 60px;
    background: radial-gradient(ellipse at 50% 45%, #6a6a6a 0%, var(--motif) 45%, rgba(94,94,94,0) 75%);
  }
  .details {
    position: absolute;
    left: 70px;
    top: 664px;
    font-family: "Montserrat", sans-serif;
  }
  .net-weight {
    font-size: 19px;
    font-weight: 600;
    color: var(--honey-cream);
    margin-bottom: 14px;
  }
  .tagline {
    font-size: 24px;
    font-weight: 600;
    letter-spacing: 2px;
    color: var(--text-light);
    margin-bottom: 6px;
  }
  .address {
    font-size: 16px;
    font-weight: 400;
    color: var(--text-muted);
  }
  .batch-code {
    position: absolute;
    right: 40px;
    top: 730px;
    font-family: "Montserrat", sans-serif;
    font-size: 22px;
    color: var(--text-muted);
    letter-spacing: 1px;
  }
</style>
</head>
<body>
<div class="canvas">
  <section class="label">
    <div class="dipper-motif" role="img" aria-label="Faint illustration of a honey dipper dripping honey into a pool"></div>
    <h1 class="brand-name">
      <span>Bright</span>
      <span>Meadow</span>
      <span>Honey</span>
    </h1>
    <div class="details">
      <p class="net-weight">500 g</p>
      <p class="tagline">LOCALLY MADE HONEY</p>
      <p class="address">48 Clover Lane, Wellington, NZ</p>
    </div>
    <p class="batch-code">123456</p>
  </section>
</div>
</body>
</html>
```